Weavers of Vigour

A book cover has already been designed, however I am looking at improving on this. The font seems a bit heavy, there is a soft and whimsical aspect to the image that is not being translated. Additionally I would like to take the green out of the title text.

The project is on hold for this cover to be completed, so we need a really quick turn around time.

The subject matter of the book is a series of photographs and conversations with some of the greatest pioneers of natural health and alternative medicine in the UK.

I have included the image to be used, which is more vibrant than the original image. Additionally I have also included a sample of the previous cover. The title, wording and strap-line needs to remain the same.

Target Market(s)

The target market of this book is predominantly female, 30 - 55 market, affluent, interested in their health and looking after themselves.

Industry/Entity Type

Alternative Medicine

Requirements
Must have
• The vibrant graphic instead of the more muted one which is currently on the cover.
Manipulation may be needed to complete the top of the head of the image.
An off white or light cream background to add some warmth.
I have provided a colour scheme below that I would like to incorporate into the title.
Additionally I would like to use a font similar to the marque foundry logo below
Final Weavers of can be in black, however I would like 'vigour' to have a similar make up as the 'Foundry' in Marque Foundry.
Should not have
• Green in either the title or the background

```html
<!DOCTYPE html>
<html lang="en">
<head>
<meta charset="utf-8">
<title>Weavers of Vigour — Book Cover</title>
<link rel="stylesheet" href="https://fonts.googleapis.com/css2?family=Encode+Sans+Condensed:wght@300;400;700&family=PT+Sans:wght@400;700&family=PT+Sans+Narrow:wght@400;700&display=swap">
<style>
  :root {
    --backdrop: #1d1c1b;
    --paper-top: #fbeadf;
    --paper-mid: #fffdfb;
    --paper-bottom: #fbe8da;
    --ink: #2a2a2a;
    --rule: #8c8c8c;
    --title-orange: #f7941d;
    --title-gold: #c9a227;
    --title-accent: #b0489a;
    --spine-accent: #b0489a;
    --art-violet: #9b6cc4;
    --art-pink: #e55aa4;
    --art-teal: #3fb6c6;
    --art-orange: #f29a3a;
  }
  * { margin: 0; padding: 0; box-sizing: border-box; }
  html, body { width: 1200px; height: 1006px; overflow: hidden; }
  body { background: var(--backdrop); font-family: "PT Sans", sans-serif; color: var(--ink); }
  .stage { position: relative; width: 1200px; height: 1006px; overflow: hidden; }

  .cover-spread {
    position: absolute; left: 83px; top: 161px; width: 1028px; height: 661px;
    background: linear-gradient(180deg, var(--paper-top) 0%, var(--paper-mid) 45%, var(--paper-mid) 60%, var(--paper-bottom) 100%);
  }
  .panel { position: absolute; top: 0; height: 100%; }
  .back-cover { left: 0; width: 482px; }
  .spine { left: 482px; width: 63px; overflow: hidden;
    background: linear-gradient(90deg, #eef3f1 0%, #fafcfb 45%, #eaf0ed 100%); }
  .front-cover { left: 545px; width: 483px; }

  .book-title {
    position: absolute; font-family: "Encode Sans Condensed", sans-serif; font-weight: 300;
    font-size: 42px; line-height: 1; letter-spacing: -0.5px; white-space: nowrap;
  }
  .book-title .w1 { color: var(--title-orange); }
  .book-title .w2 { color: var(--title-gold); }
  .book-title .w3 { color: var(--title-accent); }
  .back-cover .book-title { left: 63px; top: 70px; width: 356px; text-align: center; }
  .front-cover .book-title { left: 114px; top: 70px; width: 366px; text-align: right; }

  .byline-row { position: absolute; display: flex; align-items: flex-end; gap: 4px; height: 18px; }
  .byline-row .rule { flex: 1; border-bottom: 1px solid var(--rule); margin-bottom: 5px; }
  .byline { font-family: "PT Sans Narrow", sans-serif; font-weight: 700; font-size: 16px; line-height: 1; white-space: nowrap; }
  .back-cover .byline-row { left: 63px; top: 114px; width: 356px; }
  .front-cover .byline-row { left: 114px; top: 114px; width: 366px; }

  .blurb { position: absolute; left: 26px; width: 440px; text-align: center; font-size: 13.5px; line-height: 17.5px; }
  .blurb.intro { top: 137px; }
  .blurb.closing { top: 320px; }

  .contributors { position: absolute; left: 158px; top: 203px; font-size: 12.5px; line-height: 16px; border-collapse: collapse; }
  .contributors th { font-weight: 700; text-align: left; padding-right: 8px; }
  .contributors td { font-weight: 400; }

  .strapline { position: absolute; left: 111px; top: 146px; width: 370px;
    font-family: "PT Sans Narrow", sans-serif; font-size: 15px; line-height: 21px; }

  .spine-title { position: absolute; left: 50%; top: 118px; transform: translateX(-50%);
    writing-mode: vertical-rl; font-family: "Encode Sans Condensed", sans-serif; font-weight: 300;
    font-size: 22px; letter-spacing: 6px; white-space: nowrap; color: var(--ink); }
  .spine-title .w3 { color: var(--spine-accent); }
  .spine-byline { position: absolute; left: 50%; top: 482px; transform: translateX(-50%);
    writing-mode: vertical-rl; font-family: "PT Sans Narrow", sans-serif; font-weight: 700; font-size: 14px; white-space: nowrap; }

  .artwork { position: absolute; }
  .art-lotus-back { left: 64px; top: 360px; width: 296px; height: 301px; border-radius: 45% 45% 0 0;
    background: radial-gradient(ellipse at 55% 35%, var(--art-pink) 0%, var(--art-violet) 45%, var(--art-teal) 100%); opacity: .85; }
  .art-lotus-spine { left: 2px; top: 37px; width: 55px; height: 55px; border-radius: 50%;
    background: radial-gradient(circle, var(--art-pink), var(--art-violet) 70%); opacity: .85; }
  .art-profile { left: 0; top: 208px; width: 183px; height: 453px; border-radius: 55% 45% 0 0;
    background: linear-gradient(160deg, var(--art-violet) 0%, var(--art-pink) 35%, var(--art-teal) 65%, var(--art-orange) 100%); opacity: .85; }
  .art-lotus-front { left: 225px; top: 397px; width: 248px; height: 264px; border-radius: 45% 45% 0 0;
    background: radial-gradient(ellipse at 45% 35%, var(--art-pink) 0%, var(--art-violet) 45%, var(--art-teal) 100%); opacity: .85; }
</style>
</head>
<body>
<div class="stage">
  <div class="cover-spread">

    <section class="panel back-cover">
      <h2 class="book-title"><span class="w1">WEAVERS</span> <span class="w2">OF</span> <span class="w3">VIGOUR</span></h2>
      <div class="byline-row"><span class="rule"></span><span class="byline">by Rina Calder</span></div>
      <p class="blurb intro">Take a journey into your own body, and energy through the personal stories of some of holistic health and complementary medicine’s most expansive and creative practitioners and teachers including:</p>
      <table class="contributors">
        <tr><th>Martin Ashby</th><td>- Nutrition</td></tr>
        <tr><th>Helena Marsh</th><td>- Hypnotherapy</td></tr>
        <tr><th>Quiet Healer</th><td>- Energy Work</td></tr>
        <tr><th>Lena Harwood</th><td>- Yoga</td></tr>
        <tr><th>Carol Pemberton</th><td>- Pilates</td></tr>
        <tr><th>Joss Whitfield</th><td>- Voice Work</td></tr>
        <tr><th>Tom Brierley</th><td>- Soud Therapy</td></tr>
      </table>
      <p class="blurb closing">This book will give you an empowering 360 degree view of your own body’s natural capacity and intelligence to heal.</p>
      <div class="artwork art-lotus-back" role="img" aria-label="Illustration of two patterned hands holding a colourful lotus flower"></div>
    </section>

    <section class="panel spine">
      <div class="artwork art-lotus-spine" role="img" aria-label="Small patterned hand holding a lotus flower"></div>
      <h2 class="spine-title">WEAVERS OF <span class="w3">VIGOUR</span></h2>
      <p class="spine-byline">by Rina Calder</p>
    </section>

    <section class="panel front-cover">
      <h1 class="book-title"><span class="w1">WEAVERS</span> <span class="w2">OF</span> <span class="w3">VIGOUR</span></h1>
      <div class="byline-row"><span class="rule"></span><span class="byline">by Rina Calder</span></div>
      <p class="strapline">Complementary Therapy and Alternative Medicine thought the eyes of its practitioners and innovators.</p>
      <div class="artwork art-profile" role="img" aria-label="Vibrant patterned illustration of a woman in profile with flowing decorated hair"></div>
      <div class="artwork art-lotus-front" role="img" aria-label="Illustration of a patterned hand holding a colourful lotus flower"></div>
    </section>

  </div>
</div>
</body>
</html>
```